Lantern Hill Publicity is a new boutique Press Office with a small roster of well-chosen clients across an array of disciplines; from Art and Technology to Restaurants and Fashion. Based in Greenpoint Brooklyn, Lantern Hill Publicity achieves outstanding results through hard work, tenacity, efficiency and a sense of humor. We need a simple, versatile and classic design. We would like each side of the card to be white text on a black background.

Boutique

```html
<!DOCTYPE html>
<html lang="en">
<head>
<meta charset="utf-8">
<title>Lantern Hill Publicity — Business Card</title>
<link href="https://fonts.googleapis.com/css2?family=Cinzel:wght@400&family=Open+Sans:wght@400;600&display=swap" rel="stylesheet">
<style>
  :root {
    --backdrop: #adadad;
    --card: #141517;
    --ink: #ffffff;
    --ink-soft: #d9d9d9;
  }
  html, body {
    margin: 0;
    padding: 0;
    width: 1200px;
    height: 1200px;
    overflow: hidden;
    background: var(--backdrop);
  }
  .canvas {
    position: relative;
    width: 1200px;
    height: 1200px;
  }
  .card {
    position: absolute;
    background: var(--card);
    color: var(--ink);
  }
  .card--front {
    left: 312px;
    top: 171px;
    width: 638px;
    height: 373px;
    display: flex;
    align-items: center;
    justify-content: center;
  }
  .card--back {
    left: 314px;
    top: 586px;
    width: 625px;
    height: 384px;
  }
  .wordmark {
    display: flex;
    flex-direction: column;
    align-items: center;
    gap: 10px;
    font-family: "Cinzel", serif;
    font-weight: 400;
    color: var(--ink);
    letter-spacing: 0.16em;
    text-align: center;
    line-height: 1;
  }
  .wordmark__dot {
    width: 12px;
    height: 12px;
    border-radius: 50%;
    background: var(--ink);
    margin-bottom: 14px;
  }
  .card--front .wordmark { font-size: 29px; margin-top: 20px; }
  .card--back .wordmark {
    position: absolute;
    left: 30px;
    top: 50px;
    width: 210px;
    font-size: 21px;
    gap: 8px;
  }
  .card--back .wordmark__dot { width: 10px; height: 10px; margin-bottom: 10px; }
  .contact {
    position: absolute;
    left: 392px;
    top: 164px;
    font-family: "Open Sans", sans-serif;
    color: var(--ink);
  }
  .contact__name {
    margin: 0;
    font-size: 18px;
    font-weight: 600;
    letter-spacing: -0.01em;
  }
  .contact__role {
    margin: 2px 0 0;
    font-size: 14px;
    color: var(--ink-soft);
  }
  .contact__address {
    margin: 22px 0 0;
    font-style: normal;
    font-size: 14.5px;
    line-height: 20px;
  }
  .contact__list {
    list-style: none;
    margin: 14px 0 0;
    padding: 0;
    font-size: 14.5px;
    line-height: 21px;
  }
  .contact__list li {
    display: flex;
    align-items: center;
    gap: 8px;
  }
  .contact__icon {
    width: 12px;
    height: 12px;
    fill: var(--ink);
    flex: none;
  }
</style>
</head>
<body>
<main class="canvas">
  <section class="card card--front" aria-label="Card front">
    <div class="wordmark">
      <span class="wordmark__dot"></span>
      <span>Lantern Hill</span>
      <span>Publicity</span>
    </div>
  </section>

  <section class="card card--back" aria-label="Card back">
    <div class="wordmark">
      <span class="wordmark__dot"></span>
      <span>Lantern Hill</span>
      <span>Publicity</span>
    </div>

    <div class="contact">
      <h1 class="contact__name">Dana Whitlow</h1>
      <p class="contact__role">President</p>
      <address class="contact__address">
        48 Kent Street, Greenpoint<br>
        Brooklyn, NY 11222
      </address>
      <ul class="contact__list">
        <li>
          <svg class="contact__icon" viewBox="0 0 12 12" aria-hidden="true"><path d="M2.5 0.5l2 2.2-1 1.3c.6 1.4 1.7 2.6 3.2 3.3l1.2-1 2.3 1.9-.9 2.1C5.2 10.3 1.4 6.4.6 1.4z"/></svg>
          <span>718-555-0143</span>
        </li>
        <li>
          <svg class="contact__icon" viewBox="0 0 12 12" aria-hidden="true"><path d="M3 0h6v3H3zM0 4h12v5h-2V7H2v2H0zM3 8h6v4H3z"/></svg>
          <span>718-555-0197</span>
        </li>
        <li>
          <svg class="contact__icon" viewBox="0 0 12 12" aria-hidden="true"><path d="M0 2h12v1L6 7 0 3zM0 4.3l6 4 6-4V10H0z"/></svg>
          <span>hello@lanternhillpr.com</span>
        </li>
        <li>
          <svg class="contact__icon" viewBox="0 0 12 12" aria-hidden="true"><path d="M6 0a6 6 0 1 0 0 12A6 6 0 0 0 6 0zm0 1c.8 0 1.6 1.8 1.8 4.5H4.2C4.4 2.8 5.2 1 6 1zM1 6.5h2.2c.1 1.7.4 3.1.9 4A5 5 0 0 1 1 6.5zm0-1a5 5 0 0 1 3.1-4c-.5.9-.8 2.3-.9 4zm5 5.5c-.8 0-1.6-1.8-1.8-4.5h3.6C7.6 9.2 6.8 11 6 11zm1.9-.5c.5-.9.8-2.3.9-4H11a5 5 0 0 1-3.1 4zm.9-5c-.1-1.7-.4-3.1-.9-4A5 5 0 0 1 11 5.5z"/></svg>
          <span>www.lanternhillpr.com</span>
        </li>
      </ul>
    </div>
  </section>
</main>
</body>
</html>
```